Building Company Business Card Design

Need a design for a business card:
It needs to have: Name, Phone, Facebook link, Website, email
i would also like a list of works we undertake:
-New Homes
-Extensions, Renovations & Bathrooms
-Decking, Carports, Sheds (Residential and Industrial)
-Carpentry
-Fences, Patios & Pergolas

Name, Phone, Facebook link, Website, email + details of services provided listed in description

```html
<!DOCTYPE html>
<html lang="en">
<head>
<meta charset="utf-8">
<title>Ridgeline Homes – Business Card</title>
<link rel="stylesheet" href="https://fonts.googleapis.com/css2?family=Poppins:wght@400;500&family=Montserrat:wght@500&display=swap">
<style>
  :root {
    --page: #ffffff;
    --green-light: #7cd36a;
    --green: #33a532;
    --green-dark: #1d7a1f;
    --grey-light: #5e5f61;
    --grey: #47484a;
    --charcoal: #1e1f21;
    --text: #eeeeee;
    --text-soft: #d0d0d0;
    --rule: #3fae3a;
  }
  * { margin: 0; padding: 0; box-sizing: border-box; }
  html, body {
    width: 1200px; height: 800px; overflow: hidden;
    background: var(--page);
  }
  .canvas { position: relative; width: 1200px; height: 800px; }

  .card {
    position: absolute;
    width: 540px; height: 309px;
    border-radius: 18px;
    overflow: hidden;
    box-shadow: 0 18px 40px rgba(0,0,0,0.22);
  }
  .card-front { left: 70px; top: 70px; }
  .card-back { left: 590px; top: 420px; }
  .card-bg { position: absolute; inset: 0; width: 100%; height: 100%; }

  .brand {
    position: absolute;
    display: flex; align-items: center; gap: 10px;
    font-family: "Poppins", sans-serif;
    font-weight: 500;
    color: var(--text-soft);
  }
  .brand-mark { width: 16px; height: 16px; background: var(--green); flex: none; }
  .brand-name { display: flex; flex-direction: column; line-height: 1; }
  .brand-title { font-size: 25px; letter-spacing: 0.5px; }
  .brand-sub { font-size: 9.5px; letter-spacing: 1.4px; margin-top: 4px; }
  .card-front .brand { left: 40px; top: 125px; }
  .card-back .brand { right: 40px; top: 112px; }

  .contact {
    position: absolute; left: 300px; top: 92px; width: 220px;
    font-family: "Poppins", sans-serif;
    font-size: 13.5px; line-height: 1.5;
    color: var(--text);
  }
  .contact-label { font-style: italic; }
  .rule {
    height: 1px; width: 130px;
    background: linear-gradient(90deg, transparent, var(--rule), transparent);
  }
  .contact .rule { margin: 0 0 10px 30px; }
  .contact .rule-bottom { margin: 10px 0 0 30px; }

  .services {
    position: absolute; left: 36px; top: 62px; width: 270px;
    font-family: "Montserrat", sans-serif; font-weight: 500;
    color: var(--text);
  }
  .services-title { font-size: 22px; letter-spacing: 1.5px; font-weight: 500; }
  .services .rule { width: 170px; margin: 6px 0 12px 20px; }
  .services-list {
    list-style: none;
    font-size: 11.5px; letter-spacing: 1px; line-height: 1.55;
    color: var(--text-soft);
  }
  .services-list li { position: relative; padding-left: 18px; }
  .services-list li::before {
    content: ""; position: absolute; left: 2px; top: 7px;
    width: 4px; height: 4px; border-radius: 50%; background: var(--text-soft);
  }
  .services .rule-bottom { width: 200px; margin: 14px 0 0 50px; }
</style>
</head>
<body>
<main class="canvas">

  <section class="card card-front" aria-label="Business card front">
    <svg class="card-bg" viewBox="0 0 540 309" preserveAspectRatio="none" aria-hidden="true">
      <defs>
        <linearGradient id="front-green" x1="0" y1="0" x2="0.4" y2="1">
          <stop offset="0" stop-color="var(--green-light)"/>
          <stop offset="0.5" stop-color="var(--green)"/>
          <stop offset="1" stop-color="var(--green-dark)"/>
        </linearGradient>
        <linearGradient id="front-grey" x1="0" y1="0" x2="1" y2="1">
          <stop offset="0" stop-color="var(--charcoal)"/>
          <stop offset="0.45" stop-color="var(--grey)"/>
          <stop offset="1" stop-color="var(--grey-light)"/>
        </linearGradient>
      </defs>
      <rect width="540" height="309" fill="url(#front-green)"/>
      <circle cx="360" cy="150" r="290" fill="url(#front-grey)"/>
      <polygon points="60,60 170,40 240,90 235,250 110,270 35,200" fill="var(--charcoal)" opacity="0.85"/>
    </svg>
    <div class="brand">
      <span class="brand-mark"></span>
      <span class="brand-name">
        <span class="brand-title">RIDGELINE HOMES</span>
        <span class="brand-sub">AND BUILDS PTY LTD</span>
      </span>
    </div>
    <div class="contact">
      <div class="rule"></div>
      <p><span class="contact-label">NAME :</span> YOUR NAME</p>
      <p><span class="contact-label">PHONE :</span> 0123456789</p>
      <p><span class="contact-label">EMAIL :</span> YOUR MAIL@MAIL.COM</p>
      <p><span class="contact-label">WEBSITE :</span> WWW.WEBSITE.COM</p>
      <p><span class="contact-label">FACEBOOK :</span><br>FACEBOOK.COM/YOUR NAME</p>
      <div class="rule rule-bottom"></div>
    </div>
  </section>

  <section class="card card-back" aria-label="Business card back">
    <svg class="card-bg" viewBox="0 0 540 309" preserveAspectRatio="none" aria-hidden="true">
      <defs>
        <linearGradient id="back-green" x1="1" y1="0" x2="0.6" y2="1">
          <stop offset="0" stop-color="var(--green-light)"/>
          <stop offset="0.5" stop-color="var(--green)"/>
          <stop offset="1" stop-color="var(--green-dark)"/>
        </linearGradient>
        <linearGradient id="back-grey" x1="1" y1="0" x2="0" y2="1">
          <stop offset="0" stop-color="var(--charcoal)"/>
          <stop offset="0.45" stop-color="var(--grey)"/>
          <stop offset="1" stop-color="var(--grey-light)"/>
        </linearGradient>
      </defs>
      <rect width="540" height="309" fill="url(#back-green)"/>
      <circle cx="190" cy="150" r="300" fill="url(#back-grey)"/>
      <polygon points="300,40 420,30 505,90 500,240 380,270 300,200" fill="var(--charcoal)" opacity="0.85"/>
    </svg>
    <div class="services">
      <h2 class="services-title">OUR SERVICES</h2>
      <div class="rule"></div>
      <ul class="services-list">
        <li>NEW HOMES</li>
        <li>EXTENSIONS, RENOVATIONS<br>&amp; BATHROOMS</li>
        <li>DECKING, CARPORTS, SHEDS</li>
        <li>CARPENTRY</li>
        <li>FENCES, PATIOS &amp; PERGOLAS</li>
      </ul>
      <div class="rule rule-bottom"></div>
    </div>
    <div class="brand">
      <span class="brand-mark"></span>
      <span class="brand-name">
        <span class="brand-title">RIDGELINE HOMES</span>
        <span class="brand-sub">AND BUILDS PTY LTD</span>
      </span>
    </div>
  </section>

</main>
</body>
</html>
```